Flyer-Design für Tauchsafaris, Vollcharter und Mini Safaris am roten Meer
Zielgruppe
Koralo Diving Safari
Wir sind ein Unternehmen, welches im Roten Meer Tauchsafaris, Vollcharter und Mini Safaris durchführt. Unsere Zielgruppe sind Taucher. Wir benötigen einen ansprechenden Flyer, welchen wir an Messen und auf den Booten an pozenziellen Kunden weitergeben können.
Aufgabenstellung
Der Flyer wird in Englisch sein. Anbei ist eine Worddatei angehängt mit den Textvorschlägen, die wir mal so besprochen haben. Das Layout muss nicht beachtet werden, es hat uns nur zur Übersich gedient. Unser jetztiger Flyer ist ein Falzflyer über 6 Seiten. Aber vielleicht macht auch ein anderers Mass sinn.
Wir haben sehr viele Bilder zur Verfügung, wenn etwas spezielles gebraucht wird.

```html
<!DOCTYPE html>
<html lang="en">
<head>
<meta charset="utf-8">
<title>Koralo Diving Safari – About us</title>
<link rel="stylesheet" href="https://fonts.googleapis.com/css2?family=Nunito:wght@400;600&display=swap">
<style>
  :root {
    --navy: #1c3567;
    --ink: #24457f;
    --white: #ffffff;
    --sky-top: #6f9fd6;
    --sky-low: #b9d3ec;
    --sea: #2f6f95;
    --deck: #e9edf1;
    --crew: #5a9bd3;
  }
  * { margin: 0; padding: 0; box-sizing: border-box; }
  html, body {
    width: 1200px;
    height: 2523px;
    overflow: hidden;
    background: var(--white);
  }
  .flyer-panel {
    position: relative;
    width: 1200px;
    height: 2523px;
    background: var(--white);
    font-family: "Nunito", sans-serif;
    color: var(--ink);
  }
  .hero-photo {
    position: absolute;
    left: 0; top: 0;
    width: 1200px;
    height: 915px;
    background:
      radial-gradient(ellipse 60% 30% at 48% 62%, var(--crew) 0%, rgba(90,155,211,0) 70%),
      linear-gradient(180deg, var(--sky-top) 0%, var(--sky-low) 24%, var(--sea) 32%, var(--sea) 50%, var(--deck) 78%, #cfd6dd 100%);
  }
  .brand-tag {
    position: absolute;
    left: 0; top: 42px;
    width: 385px;
    height: 106px;
    background: var(--white);
    display: flex;
    align-items: center;
    padding-left: 26px;
    gap: 16px;
  }
  .brand-dot {
    width: 64px; height: 64px;
    border-radius: 50%;
    background: var(--navy);
    flex: none;
  }
  .brand-name {
    font-size: 25px;
    font-weight: 600;
    color: var(--navy);
    line-height: 1.1;
  }
  .brand-sub {
    display: block;
    font-size: 15px;
    font-weight: 600;
    color: var(--navy);
    letter-spacing: 1px;
    margin-top: 4px;
  }
  .about {
    position: absolute;
    left: 106px;
    top: 950px;
    width: 1040px;
  }
  .about-title {
    font-size: 66px;
    font-weight: 600;
    color: var(--navy);
    line-height: 1.2;
    margin-bottom: 2px;
  }
  .about-text {
    font-size: 44px;
    font-weight: 400;
    line-height: 59px;
    margin-bottom: 59px;
  }
</style>
</head>
<body>
  <main class="flyer-panel">
    <div class="hero-photo" role="img" aria-label="Photo of the smiling diving crew in blue shirts holding a company banner on the deck of a safari boat, with boats and the Red Sea behind"></div>

    <div class="brand-tag">
      <span class="brand-dot"></span>
      <span class="brand-name">Koralo Diving Safari<span class="brand-sub">RED SEA DIVING</span></span>
    </div>

    <section class="about">
      <h1 class="about-title">About us</h1>
      <p class="about-text">For more than 7 years we have been proud to<br>arrange your diving adventure in the Red Sea of<br>Egypt. Made by divers, for divers with more than<br>10 years of experience.</p>
      <p class="about-text">We are specialized in diving safaris,<br>full charter and mini safaris. Our ultimate<br>ambition is to make your wishes come true.</p>
      <p class="about-text">Whether you are an experienced diver or have<br>just started your diving adventure. We want to<br>take you away from everyday life and immerse<br>you in the colourful world of corals and fish.</p>
      <p class="about-text">Our team is at home in the Red Sea and knows<br>the finest places and shows you with passion the<br>variety of countless dive sites coasts nearby and<br>far.</p>
    </section>
  </main>
</body>
</html>
```